Brivora Healthcare Services ( a Communitiy Mental Health Services with a full continuum of services

Our company colors are esspresso brown and french vanilla. Our message is "Your partner in Healthcare" This is the individual client's partner and other community agencies' partner. Some fresh green to express new growth or new beginnings or healing could be used - as well as other colors as long as the main colors are company colors.
We provide Outpatient Treatment for mental health and substance abuse disorders. We also have a Crisis continuum that includes a Walk-In assessment center, Mobile Crisis, Crisis Stabilazation, Medically Monitored Detox and Respite.
We have been in business over 30 years and want to send the message of being a solid, forward thinking, cutting edge, provider who focuses on quality and evidenced based treatment.
The attachment includes our logo that must be used. The wording only includes the Crisis continuum - except the part that describes the company on the back page.

Industry/Entity Type

Healthcare

```html
<!DOCTYPE html>
<html lang="en">
<head>
<meta charset="utf-8">
<title>Brivora Healthcare Services – Tri-fold Brochure</title>
<link rel="stylesheet" href="https://fonts.googleapis.com/css2?family=Open+Sans:ital,wght@0,400;0,600;0,700;1,600&display=swap">
<style>
  :root{
    --stage:#0f5d7c;
    --espresso:#4e3436;
    --espresso-deep:#3c282a;
    --espresso-light:#6b4a4c;
    --vanilla:#f4e7a6;
    --vanilla-soft:#f8efc4;
    --ink-light:#efe4d4;
    --frame:#3a2527;
  }
  *{box-sizing:border-box;margin:0;padding:0}
  html,body{width:1200px;height:934px;overflow:hidden}
  body{background:var(--stage);font-family:"Open Sans",Arial,sans-serif;position:relative}

  .sheet{position:absolute;display:flex;box-shadow:0 12px 24px rgba(0,0,0,.35)}
  .sheet--outside{left:270px;top:164px;width:660px;height:294px}
  .sheet--inside{left:278px;top:505px;width:618px;height:297px}

  .panel{position:relative;height:100%;overflow:hidden;background:linear-gradient(160deg,var(--espresso-light),var(--espresso) 55%,var(--espresso-deep))}
  .sheet--outside .panel{width:220px}
  .sheet--inside .panel{width:206px}
  .panel--dark{background:linear-gradient(170deg,var(--espresso),var(--espresso-deep))}
  .panel + .panel{border-left:1px solid rgba(0,0,0,.18)}

  .shape{position:absolute;inset:0;width:100%;height:100%}
  .shape path{fill:var(--vanilla)}

  .photo{position:absolute;border:3px solid var(--vanilla);border-radius:7px;box-shadow:0 0 0 2px var(--frame)}
  .photo--hands{background:radial-gradient(circle at 50% 50%,#f3ece4 0 26%,#c98f63 30%,#8a5436 80%)}
  .photo--map{background:linear-gradient(135deg,#ece8dc,#d9d4c4 60%,#cfe2b8)}
  .photo--house{background:linear-gradient(180deg,#8fb8e2 0,#b7cfe6 40%,#d9d2c2 55%,#5f8a3c 75%,#3f6a28)}
  .photo--people{background:linear-gradient(90deg,#d8c9b8,#8c6a58 40%,#e6dccd 70%,#6d4f44)}

  .brand{position:absolute;color:var(--ink-light);font-weight:600;letter-spacing:.5px;text-align:center}
  .brand__tag{display:block;font-size:5px;font-weight:400;letter-spacing:.2px;margin-top:2px}
  .brand--hero{left:0;right:0;top:150px;font-size:34px;font-weight:600}
  .brand--hero .brand__tag{font-size:6px;margin-top:4px}
  .brand--small{font-size:13px}
  .tagline{position:absolute;left:0;right:0;top:240px;text-align:center;color:var(--ink-light);font-size:9px;font-style:italic;font-weight:600}

  .heading{color:var(--ink-light);font-weight:700;font-size:8.5px;letter-spacing:.2px;text-transform:uppercase;text-align:center}
  .copy{color:var(--ink-light);font-size:5.4px;line-height:1.45;text-align:justify}
  .copy p + p{margin-top:9px}
  .bullets{list-style:none;color:var(--ink-light);font-size:5.4px;line-height:1.45;text-align:justify}
  .bullets li{position:relative;padding-left:7px;margin-top:8px}
  .bullets li::before{content:"";position:absolute;left:0;top:2px;width:3px;height:3px;border-radius:50%;background:var(--vanilla)}

  .contact{position:absolute;left:50px;top:228px;color:var(--ink-light);font-size:5.4px;line-height:1.5;font-weight:600;text-transform:uppercase;font-style:normal}
  .backdrop{position:absolute;inset:0;background:linear-gradient(180deg,rgba(255,255,255,.06),rgba(120,150,110,.10) 50%,rgba(0,0,0,0));}
</style>
</head>
<body>

<section class="sheet sheet--outside">
  <article class="panel panel--cover">
    <svg class="shape" viewBox="0 0 220 294" preserveAspectRatio="none">
      <path d="M0 0H220V96Q120 126 0 118Z"/>
      <path d="M0 294V250Q60 268 112 294Z"/>
    </svg>
    <div class="photo photo--hands" style="left:8px;top:38px;width:56px;height:64px" role="img" aria-label="Photo of hands joined in a circle"></div>
    <div class="photo photo--hands" style="left:72px;top:38px;width:64px;height:64px" role="img" aria-label="Photo of hands forming a heart"></div>
    <div class="brand brand--hero">Brivora<span class="brand__tag">Brivora Healthcare Services</span></div>
    <div class="tagline">“Your Partner in Healthcare”</div>
  </article>

  <article class="panel panel--dark">
    <svg class="shape" viewBox="0 0 220 294" preserveAspectRatio="none">
      <path d="M220 294V248Q160 272 120 294Z"/>
    </svg>
    <div style="position:absolute;left:18px;right:18px;top:16px">
      <h2 class="heading">Brivora Healthcare Services</h2>
      <div class="copy" style="margin-top:12px">
        <p>Brivora Healthcare Services has supported our community for over thirty years with outpatient treatment for mental health and substance use disorders, built on quality and evidence based care.</p>
        <p>Our crisis continuum offers a walk-in assessment center, mobile crisis teams, crisis stabilization, medically monitored detox and respite, so help is ready whenever and wherever it is needed.</p>
        <p>We partner with each client and with agencies across the region, working side by side to build recovery, restore stability and open the door to new beginnings.</p>
      </div>
    </div>
    <div class="brand brand--small" style="left:18px;top:226px;text-align:left">Brivora<span class="brand__tag">Your Partner in Healthcare</span></div>
  </article>

  <article class="panel">
    <svg class="shape" viewBox="0 0 220 294" preserveAspectRatio="none">
      <path d="M0 0H150Q70 14 0 34Z"/>
      <path d="M0 294V262Q40 276 70 294Z"/>
    </svg>
    <div class="brand brand--small" style="right:18px;top:14px">Brivora<span class="brand__tag">Your Partner in Healthcare</span></div>
    <div class="photo photo--map" style="left:40px;top:82px;width:96px;height:98px" role="img" aria-label="Street map showing the office location"></div>
    <div class="photo photo--house" style="left:16px;top:211px;width:88px;height:70px" role="img" aria-label="Photo of a house with a lawn"></div>
    <div class="photo photo--house" style="left:112px;top:211px;width:86px;height:70px" role="img" aria-label="Photo of a two-storey home with trees"></div>
  </article>
</section>

<section class="sheet sheet--inside">
  <article class="panel">
    <svg class="shape" viewBox="0 0 206 297" preserveAspectRatio="none">
      <path d="M0 104Q110 96 206 118V150Q100 132 0 150Z"/>
    </svg>
    <div class="photo photo--people" style="left:16px;top:19px;width:108px;height:70px" role="img" aria-label="Photo of smiling people joining hands"></div>
    <div class="brand brand--small" style="left:132px;top:28px">Brivora<span class="brand__tag">Your Partner in Healthcare</span></div>
    <div style="position:absolute;left:16px;right:16px;top:154px">
      <h2 class="heading">Brivora Healthcare Services</h2>
      <ul class="bullets">
        <li>Walk-in assessment center open to adults and youth seeking same day evaluation and support.</li>
        <li>Mobile crisis teams meet people at home, school or work when a situation cannot wait.</li>
        <li>Trained clinicians respond quickly and link each person to the right level of care.</li>
      </ul>
    </div>
  </article>

  <article class="panel panel--dark">
    <div class="backdrop" role="img" aria-label="Faint photo of a home and trees behind the text"></div>
    <svg class="shape" viewBox="0 0 206 297" preserveAspectRatio="none">
      <path d="M0 297V262Q50 276 96 297Z"/>
    </svg>
    <div style="position:absolute;left:16px;right:16px;top:22px">
      <h2 class="heading">Brivora Healthcare Services</h2>
      <ul class="bullets">
        <li>Crisis stabilization offers a calm, safe setting for short term care and close support.</li>
        <li>Medically monitored detox provides round the clock nursing during withdrawal.</li>
        <li>Each plan is shaped with the client and family to prepare for the next step.</li>
      </ul>
    </div>
    <div class="brand brand--small" style="left:120px;top:184px">Brivora<span class="brand__tag">Your Partner in Healthcare</span></div>
    <div class="photo photo--hands" style="left:18px;top:186px;width:62px;height:76px" role="img" aria-label="Photo of hands forming a heart"></div>
  </article>

  <article class="panel">
    <svg class="shape" viewBox="0 0 206 297" preserveAspectRatio="none">
      <path d="M0 0H206V16Q100 8 0 24Z"/>
      <path d="M0 297V276Q30 286 56 297Z"/>
    </svg>
    <div style="position:absolute;left:16px;right:16px;top:30px">
      <h2 class="heading">Brivora Healthcare Services</h2>
      <ul class="bullets">
        <li>Respite care gives individuals a supportive place to rest, recover and regain balance.</li>
        <li>Our staff coordinate with partner agencies so no one falls through the cracks.</li>
        <li>Evidence based practices guide every service we deliver.</li>
      </ul>
    </div>
    <div class="brand brand--small" style="left:60px;top:188px">Brivora<span class="brand__tag">Your Partner in Healthcare</span></div>
    <div class="photo photo--hands" style="left:140px;top:206px;width:54px;height:50px" role="img" aria-label="Photo of hands joined in a circle"></div>
    <address class="contact">
      Brivora Healthcare Services<br>
      1420 Maple Ridge Drive<br>
      Suite 200<br>
      Fairhaven, OH 45210<br>
      Tel: (555) 014-2290
    </address>
  </article>
</section>

</body>
</html>
```